RallyLot Spaces iPhone App Splash Page and Company Logo

RallyLot Spaces has developed several iPhone applications to help college football (American football, not European football/soccer) fans find parking on game days. The current logo and several splash pages are included here.

We are looking for an updated/fresh logo for our new "universal" app - a single iPhone app that provides information for all college football venues (currently there is a separate app for each venue). Specifically, we need an iPhone splash page design that allows space for several (3) buttons on the right side of the splash screen (much like the placement of the buttons on the current splash screens shown). We also need a logo that can work as an iPhone app icon.

The theme should reflect college football, parking, and efficiency.

Target Market(s)

College graduates attending saturday football games.

Industry/Entity Type

College

Logo Text

College Football RallyLot Spaces

Requirements
Must have
• Clean. Simple. Collegiate feel.

```html
<!DOCTYPE html>
<html lang="en">
<head>
<meta charset="utf-8">
<title>RallyLot Spaces – Splash Page and Logo</title>
<link rel="stylesheet" href="https://fonts.googleapis.com/css2?family=Varela+Round&display=swap">
<style>
  :root {
    --canvas-bg: #ffffff;
    --asphalt-dark: #1c1c1c;
    --asphalt-mid: #2e2e2e;
    --brand-green: #00ad6f;
    --brand-navy: #0d2147;
    --text-light: #ffffff;
  }
  * { margin: 0; padding: 0; box-sizing: border-box; }
  html, body {
    width: 1200px;
    height: 675px;
    overflow: hidden;
    background: var(--canvas-bg);
    font-family: "Varela Round", sans-serif;
  }
  .canvas {
    position: relative;
    width: 1200px;
    height: 675px;
  }

  /* Splash screen */
  .splash {
    position: absolute;
    left: 232px;
    top: 165px;
    width: 223px;
    height: 375px;
    overflow: hidden;
  }
  .splash-surface {
    position: absolute;
    inset: 0;
    background: radial-gradient(circle at 40% 35%, var(--asphalt-mid), var(--asphalt-dark) 75%);
  }
  .splash-brand {
    position: absolute;
    left: 0;
    top: 40px;
    width: 174px;
    display: flex;
    flex-direction: column;
    align-items: center;
    gap: 8px;
  }
  .splash-brand .brand-dot {
    width: 54px;
    height: 54px;
    border-radius: 50%;
    background: var(--brand-green);
  }
  .splash-brand .brand-name {
    color: var(--text-light);
    font-size: 15px;
    white-space: nowrap;
  }
  .venue-name {
    position: absolute;
    left: 49px;
    top: 363px;
    transform-origin: 0 0;
    transform: rotate(-90deg) translateY(-50%);
    color: var(--text-light);
    font-size: 35px;
    font-weight: 400;
    white-space: nowrap;
    line-height: 1;
  }
  .menu-button {
    position: absolute;
    width: 170px;
    height: 36px;
    margin-top: -18px;
    border-radius: 18px 0 0 18px;
    transform-origin: 0 50%;
    transform: rotate(-28deg);
    color: var(--text-light);
    font-size: 12px;
    line-height: 36px;
    padding-left: 20px;
    white-space: nowrap;
  }
  .menu-button--park { left: 114px; top: 221px; background: var(--brand-navy); }
  .menu-button--info { left: 114px; top: 278px; background: var(--brand-green); }
  .menu-button--about { left: 132px; top: 322px; background: var(--brand-navy); }

  /* Company logo */
  .logo-lockup {
    position: absolute;
    left: 860px;
    top: 312px;
    transform: translate(-50%, -50%);
    display: flex;
    flex-direction: column;
    align-items: center;
    gap: 18px;
  }
  .logo-lockup .brand-dot {
    width: 150px;
    height: 150px;
    border-radius: 50%;
    background: var(--brand-green);
  }
  .logo-lockup .brand-name {
    color: var(--brand-green);
    font-size: 34px;
    white-space: nowrap;
  }
</style>
</head>
<body>
  <main class="canvas">
    <section class="splash" aria-label="Splash page">
      <div class="splash-surface" role="img" aria-label="Dark asphalt texture background"></div>
      <div class="splash-brand">
        <span class="brand-dot"></span>
        <span class="brand-name">RallyLot Spaces</span>
      </div>
      <h1 class="venue-name">All Venues</h1>
      <nav>
        <a class="menu-button menu-button--park">Where To Park</a>
        <a class="menu-button menu-button--info">Game Day Info</a>
        <a class="menu-button menu-button--about">About Us</a>
      </nav>
    </section>

    <section class="logo-lockup" aria-label="Company logo">
      <span class="brand-dot"></span>
      <span class="brand-name">RallyLot Spaces</span>
    </section>
  </main>
</body>
</html>
```